Kovalen Spinal Care and Performance

We need new business cards, something more modern, clean. On the back of the card maybe a quote. The Dr. likes, “The doctor of the future will give no medicine, but will interest his patient in the care of the human frame, in diet and in the cause and prevention of disease.” - Walter Brisby. We are open to other suggestions. We are a chiropractic office.

```html
<!DOCTYPE html>
<html lang="en">
<head>
<meta charset="utf-8">
<title>Kovalen Spinal Care and Performance — Business Cards</title>
<link rel="stylesheet" href="https://fonts.googleapis.com/css2?family=Oswald:wght@500;600&family=Poppins:wght@400;500&display=swap">
<style>
  :root {
    --backdrop: #e6e6e8;
    --card-purple: #45134d;
    --text-light: #ffffff;
    --text-soft: #f1e6f4;
    --brand-lilac: #a463c4;
    --divider: rgba(255, 255, 255, 0.7);
  }
  * { margin: 0; padding: 0; box-sizing: border-box; }
  html, body {
    width: 1200px;
    height: 800px;
    overflow: hidden;
    background: var(--backdrop);
  }
  .canvas {
    position: relative;
    width: 1200px;
    height: 800px;
    display: flex;
    align-items: center;
    justify-content: center;
    gap: 40px;
  }
  .card {
    position: relative;
    width: 540px;
    height: 310px;
    background: var(--card-purple);
    border-radius: 22px;
    color: var(--text-light);
    overflow: hidden;
  }

  /* Contact side */
  .identity {
    position: absolute;
    right: 300px;
    top: 92px;
    text-align: right;
    font-family: "Oswald", sans-serif;
    text-transform: uppercase;
    line-height: 1.05;
  }
  .identity .person-name { font-size: 22px; font-weight: 600; letter-spacing: 0.5px; }
  .identity .person-role { font-size: 16px; font-weight: 500; letter-spacing: 0.6px; }
  .divider {
    position: absolute;
    left: 262px;
    top: 70px;
    width: 1px;
    height: 108px;
    background: var(--divider);
  }
  .contact-list {
    position: absolute;
    left: 280px;
    top: 72px;
    list-style: none;
    font-family: "Poppins", sans-serif;
    font-size: 13px;
    line-height: 20.5px;
    color: var(--text-soft);
  }
  .contact-list li { display: flex; align-items: center; gap: 8px; }
  .icon { width: 11px; height: 11px; flex: none; fill: var(--text-light); }
  .address {
    position: absolute;
    left: 0;
    right: 0;
    bottom: 34px;
    display: flex;
    justify-content: center;
    align-items: center;
    gap: 8px;
    font-family: "Poppins", sans-serif;
    font-size: 13px;
    color: var(--text-soft);
  }

  /* Brand side */
  .brand-name {
    position: absolute;
    left: 0;
    right: 0;
    top: 62px;
    text-align: center;
    font-family: "Poppins", sans-serif;
    font-weight: 500;
    color: var(--brand-lilac);
    font-size: 22px;
    line-height: 1.3;
    letter-spacing: 0.4px;
  }
  .quote {
    position: absolute;
    left: 30px;
    right: 30px;
    bottom: 44px;
    text-align: center;
    font-family: "Poppins", sans-serif;
    font-size: 12.5px;
    line-height: 19px;
    color: var(--text-soft);
  }
</style>
</head>
<body>
<main class="canvas">

  <section class="card card--contact" aria-label="Business card, contact side">
    <div class="identity">
      <p class="person-name">Daniel Reyes</p>
      <p class="person-role">President</p>
    </div>
    <div class="divider"></div>
    <ul class="contact-list">
      <li>
        <svg class="icon" viewBox="0 0 12 12" aria-hidden="true"><path d="M2.4 0.6l2 2-1.1 1.4c.7 1.6 2 2.9 3.6 3.6l1.4-1.1 2 2-1.4 2.1C5.1 10.4 1.6 6.9 0.4 2z"/></svg>
        555-214-7730
      </li>
      <li>
        <svg class="icon" viewBox="0 0 12 12" aria-hidden="true"><path d="M3 0.5h6v11H3z M4 1.5v8h4v-8z" fill-rule="evenodd"/></svg>
        555-308-4192
      </li>
      <li>
        <svg class="icon" viewBox="0 0 12 12" aria-hidden="true"><path d="M3 0.5h5v3H3z M1 4.5h10v6H1z"/></svg>
        555-611-2085
      </li>
      <li>
        <svg class="icon" viewBox="0 0 12 12" aria-hidden="true"><path d="M0.5 2h11v8h-11z M1.5 3l4.5 3.5L10.5 3" fill-rule="evenodd"/></svg>
        info@kovalen.com
      </li>
      <li>
        <svg class="icon" viewBox="0 0 12 12" aria-hidden="true"><circle cx="6" cy="6" r="5.5"/></svg>
        www.kovalen.com
      </li>
    </ul>
    <p class="address">
      <svg class="icon" viewBox="0 0 12 12" aria-hidden="true"><path d="M6 0.3a4 4 0 0 1 4 4c0 3-4 7.4-4 7.4S2 7.3 2 4.3a4 4 0 0 1 4-4z M6 2.6a1.7 1.7 0 1 0 0 3.4a1.7 1.7 0 0 0 0-3.4z" fill-rule="evenodd"/></svg>
      4120 Maple Ridge Road, Fairview, Oregon 97024
    </p>
  </section>

  <section class="card card--brand" aria-label="Business card, brand side">
    <p class="brand-name">Kovalen<br>Spinal Care and Performance</p>
    <p class="quote">“The doctor of the future will give no medicine,<br>but will interest his patient in the care of the human frame,<br>in diet and in the cause and prevention of disease.” – Walter Brisby.</p>
  </section>

</main>
</body>
</html>
```